indépendant en tant que Massothérapeute et Préparateur Mental, j'ai besoin de ...

Massothérapeute et préparateur mental indépendant, je recherche une carte de visite sobre et dynamique, sans images liées au massage ou à la préparation mentale mais intégrant mon logo. Les couleurs que j'aime bien sont : Blanc, gris, anthracite, noir et jaune

Contact Information for Business Card

carte de préférence Horizontale
neutre qui puisse toucher le deux domaines Massothérapie et préparation mentale

Requirements
Must have
• mon projet doit intégrer au recto:
LOGO
Loïc Vermande
078 315 26 49
info@loicvermande-exemple.ch
et éventuellement www.loicvermande-exemple.ch

et au verso les deux adresses:

Chemin des Ormelets 27B
1400 Yverdon-les-Bains

Rue des Tanneries 9
1700 Fribourg

Should not have
• mon projet ne doit pas contenir d'image en liens avec le massage ni la préparation mentale.

```html
<!DOCTYPE html>
<html lang="fr">
<head>
<meta charset="utf-8">
<title>Loïc Vermande – Carte de visite</title>
<link rel="stylesheet" href="https://fonts.googleapis.com/css2?family=Lato:wght@300;400;700&display=swap">
<style>
  :root {
    --backdrop: #3a3a3a;
    --card: #262626;
    --card-back: #222222;
    --mark: #4a4a4a;
    --text-strong: #f2f2f2;
    --text-soft: #b5b5b5;
    --text-muted: #8a8a8a;
    --rule: #6a6a6a;
  }
  * { margin: 0; padding: 0; box-sizing: border-box; }
  html, body { width: 1200px; height: 900px; overflow: hidden; }
  body {
    background: var(--backdrop);
    font-family: "Lato", sans-serif;
    position: relative;
  }
  .card {
    position: absolute;
    width: 525px;
    height: 300px;
    box-shadow: 0 12px 30px rgba(0,0,0,0.45);
  }
  .card--front { left: 50px; top: 300px; background: var(--card); }
  .card--back  { left: 625px; top: 300px; background: var(--card-back); }

  .brand {
    position: absolute;
    left: 48px;
    top: 104px;
    display: flex;
    align-items: center;
    gap: 18px;
  }
  .brand__square {
    width: 44px; height: 44px;
    background: var(--mark);
  }
  .brand__name {
    font-size: 22px;
    font-weight: 700;
    color: var(--text-strong);
    letter-spacing: 0.5px;
  }
  .tagline {
    position: absolute;
    left: 238px;
    top: 136px;
    font-size: 9px;
    font-variant: small-caps;
    letter-spacing: 0.6px;
    color: var(--text-soft);
  }
  .rule {
    height: 1px;
    width: 62px;
    background: linear-gradient(90deg, var(--rule), transparent);
  }
  .front-details {
    position: absolute;
    left: 238px;
    top: 158px;
  }
  .front-details .rule { margin-bottom: 14px; }
  .contact-name {
    font-size: 14px;
    font-weight: 700;
    color: var(--text-strong);
    margin-bottom: 10px;
  }
  .contact-list { list-style: none; }
  .contact-list li {
    display: flex;
    align-items: center;
    gap: 9px;
    font-size: 12px;
    color: var(--text-soft);
    line-height: 19px;
  }
  .contact-list svg { width: 10px; height: 10px; flex: none; }

  .addresses {
    position: absolute;
    left: 262px;
    top: 118px;
    font-size: 12px;
    line-height: 16px;
    color: var(--text-soft);
  }
  .addresses .rule { margin: 9px 0 10px; }
</style>
</head>
<body>
  <section class="card card--front" aria-label="Recto de la carte">
    <div class="brand">
      <span class="brand__square"></span>
      <span class="brand__name">Loïc Vermande</span>
    </div>
    <p class="tagline">Massothérapeute / Préparateur Mental</p>
    <div class="front-details">
      <div class="rule"></div>
      <p class="contact-name">Loïc Vermande</p>
      <ul class="contact-list">
        <li>
          <svg viewBox="0 0 10 10" aria-hidden="true"><rect x="2.5" y="0.5" width="5" height="9" rx="1" fill="none" stroke="#d0d0d0"/><circle cx="5" cy="8" r="0.6" fill="#d0d0d0"/></svg>
          078 315 26 49
        </li>
        <li>
          <svg viewBox="0 0 10 10" aria-hidden="true"><rect x="0.5" y="2" width="9" height="6" fill="#d0d0d0"/><path d="M0.5 2 L5 5.5 L9.5 2" fill="none" stroke="#262626"/></svg>
          info@loicvermande-exemple.ch
        </li>
        <li>
          <svg viewBox="0 0 10 10" aria-hidden="true"><circle cx="5" cy="5" r="4.3" fill="none" stroke="#d0d0d0"/><ellipse cx="5" cy="5" rx="1.8" ry="4.3" fill="none" stroke="#d0d0d0"/><path d="M0.7 5 H9.3" stroke="#d0d0d0"/></svg>
          www.loicvermande-exemple.ch
        </li>
      </ul>
    </div>
  </section>

  <section class="card card--back" aria-label="Verso de la carte">
    <address class="addresses" style="font-style:normal">
      <p>Chemin des Ormelets 27B<br>1400 Yverdon-les-Bains</p>
      <div class="rule"></div>
      <p>Rue des Tanneries 9<br>1700 Fribourg</p>
    </address>
  </section>
</body>
</html>
```